Professional Stationery Design - 16062020

Professional Logo, BCard, Email Signature & Letterhead design. This is the stationary design project for a professional Management Services Company

Target Market(s)

All

Industry/Entity Type

Management Solution

Requirements
Must have
• Professional

```html
<!DOCTYPE html>
<html lang="en">
<head>
<meta charset="utf-8">
<title>Corvella Management Services — Stationery</title>
<link rel="stylesheet" href="https://fonts.googleapis.com/css2?family=Poppins:wght@400;500;600;700&family=Source+Sans+3:wght@400&display=swap">
<style>
:root{
  --orange:#f26a1b;
  --ink:#1d1d1f;
  --black:#141414;
  --paper:#ffffff;
  --backdrop:#ececec;
  --rule:#3a3a3a;
  --muted:#555;
}
*{box-sizing:border-box;margin:0;padding:0}
html,body{width:1035px;height:1200px;overflow:hidden}
body{background:var(--backdrop);position:relative;font-family:"Poppins",sans-serif;color:var(--ink)}
.sheet{position:absolute;background:var(--paper);box-shadow:0 2px 6px rgba(0,0,0,.18);overflow:hidden}
.brand{position:absolute;line-height:1}
.brand-name{display:block;font-weight:600;color:var(--ink);letter-spacing:.06em}
.brand-tag{display:block;color:var(--orange);letter-spacing:.22em;font-weight:500;margin-top:2px}
.swoosh{position:absolute;left:0;bottom:0;width:100%;display:block}
.icon{fill:var(--orange);vertical-align:middle}

/* business cards */
.card{width:176px;height:102px;border-radius:6px}
.card-front{left:99px;top:96px}
.card-back{left:306px;top:96px;background:var(--black)}
.card-front .brand{left:10px;top:38px}
.card-front .brand-name{font-size:13px}
.card-front .brand-tag{font-size:3.6px}
.card-divider{position:absolute;left:92px;top:22px;width:1px;height:42px;background:var(--orange)}
.card-details{position:absolute;left:97px;top:20px;font-size:4.2px;line-height:6.2px}
.card-details .person{font-size:7px;font-weight:600;line-height:8px}
.card-details .role{color:var(--orange);font-size:4.2px;font-weight:500}
.card-details .web span{color:var(--orange)}
.card-back .brand{left:0;right:0;top:38px;text-align:center}
.card-back .brand-name{font-size:17px;color:#3a3a3a}
.card-back .brand-tag{font-size:4.4px}
.card-back .card-web{position:absolute;bottom:10px;width:100%;text-align:center;color:#d0d0d0;font-size:4.4px;letter-spacing:.05em}

/* letterheads */
.letterhead{top:248px;height:516px}
.lh-plain{left:106px;width:365px}
.lh-word{left:544px;width:400px}
.letterhead .brand{left:23px;top:39px}
.letterhead .brand-name{font-size:22px}
.letterhead .brand-tag{font-size:5.4px}
.lh-contact{position:absolute;top:34px;right:22px;border-left:1px solid var(--rule);padding-left:5px;font-size:7.2px;line-height:10.4px}
.lh-contact .line{display:flex;align-items:center;gap:3px}
.lh-contact .web span{color:var(--orange)}
.lh-footer{position:absolute;left:23px;right:20px;top:442px;display:flex}
.office{font-size:6.8px;line-height:10px;padding-right:8px}
.office + .office{border-left:1px solid var(--rule);padding-left:8px}
.office-title{color:var(--orange);font-weight:500}
.office .line{display:flex;align-items:center;gap:3px}
.lh-plain .office:nth-child(1){width:124px}.lh-plain .office:nth-child(2){width:113px}
.lh-word .office:nth-child(1){width:137px}.lh-word .office:nth-child(2){width:143px}
.letter{position:absolute;left:25px;right:25px;top:112px;font-size:6.4px;line-height:10.3px}
.letter .salutation{color:var(--orange)}
.letter .recipient{margin-bottom:16px}
.letter p.body{text-align:justify;margin-bottom:10px}
.letter .closing{margin-top:12px}
.signature{width:50px;height:14px;margin-top:4px;background:linear-gradient(90deg,#e6e6e6,#f4f4f4);border-radius:2px}

.label{position:absolute;top:797px;font-family:"Source Sans 3",sans-serif;color:var(--orange);font-size:18px}
.label-plain{left:223px}
.label-word{left:655px}

/* email signature */
.email-signature{left:106px;top:881px;width:842px;height:193px}
.email-signature .brand{left:235px;top:78px}
.email-signature .brand-name{font-size:32px}
.email-signature .brand-tag{font-size:8.2px;margin-top:3px}
.sig-divider{position:absolute;left:444px;top:28px;width:1.5px;height:132px;background:var(--orange)}
.sig-details{position:absolute;left:464px;top:27px;font-size:11px;line-height:16.6px}
.sig-details .person{font-size:16px;font-weight:600;line-height:20px}
.sig-details .role{color:var(--orange);font-size:10px;font-weight:500;margin-bottom:3px}
.sig-details .line{display:flex;align-items:center;gap:8px}
.sig-details .web{letter-spacing:.06em}
.social{position:absolute;left:12px;bottom:12px;display:flex;gap:16px}
.social span{width:14px;height:14px;border-radius:50%;background:var(--orange)}
</style>
</head>
<body>

<svg width="0" height="0" style="position:absolute" aria-hidden="true">
  <defs>
    <symbol id="i-phone" viewBox="0 0 10 10"><path d="M2 0.5l2 2-1 1.2c.6 1.3 1.6 2.3 2.9 2.9l1.2-1 2 2-1.3 1.6C4.2 9 1 5.8.8 1.8z"/></symbol>
    <symbol id="i-fax" viewBox="0 0 10 10"><path d="M2.5 0h5v3h-5zM0 3.5h10v4.5H8V6H2v2H0zM2.5 6.8h5V10h-5z"/></symbol>
    <symbol id="i-mail" viewBox="0 0 10 10"><path d="M0 2h10v6H0zm1 1v.3l4 2.6 4-2.6V3zM1 4.5V7h8V4.5L5 7z" fill-rule="evenodd"/></symbol>
    <symbol id="i-web" viewBox="0 0 10 10"><circle cx="5" cy="5" r="4.5"/><path d="M0.5 5h9M5 .5c-2.4 2.6-2.4 6.4 0 9M5 .5c2.4 2.6 2.4 6.4 0 9" stroke="#fff" stroke-width=".7" fill="none"/></symbol>
    <symbol id="i-doc" viewBox="0 0 10 10"><path d="M1.5 0h5l2 2v8h-7zM3 4h4v.8H3zm0 2h4v.8H3z" fill-rule="evenodd"/></symbol>
    <symbol id="band" viewBox="0 0 400 30" preserveAspectRatio="none">
      <path d="M0 4C110 16 250 24 400 23V30H0Z" fill="#141414"/>
      <path d="M0 10C120 20 240 26 330 27H0Z" fill="#2c2c2c"/>
      <path d="M170 27C270 24 340 16 400 6V13C340 21 270 27 170 28Z" fill="#f26a1b"/>
    </symbol>
  </defs>
</svg>

<!-- Business card, front -->
<section class="sheet card card-front">
  <div class="brand"><span class="brand-name">CORVELLA</span><span class="brand-tag">MANAGEMENT SERVICES</span></div>
  <div class="card-divider"></div>
  <div class="card-details">
    <div class="person">DANIEL OKORO</div>
    <div class="role">HEAD OF ICT</div>
    <div>24 Kestrel Road, Parkview</div>
    <div>Johannesburg, 2193</div>
    <div><svg class="icon" width="4" height="4"><use href="#i-phone"/></svg> 085 410 7723</div>
    <div><svg class="icon" width="4" height="4"><use href="#i-phone"/></svg> 011 502 3391</div>
    <div><svg class="icon" width="4" height="4"><use href="#i-mail"/></svg> it@corvellams.com</div>
    <div class="web"><svg class="icon" width="4" height="4"><use href="#i-web"/></svg> www.<span>corvellams</span>.com</div>
  </div>
  <svg class="swoosh" height="16"><use href="#band"/></svg>
</section>

<!-- Business card, back -->
<section class="sheet card card-back">
  <div class="brand"><span class="brand-name">CORVELLA</span><span class="brand-tag">MANAGEMENT SERVICES</span></div>
  <div class="card-web">www.corvellams.com</div>
</section>

<!-- Letterhead, blank -->
<section class="sheet letterhead lh-plain">
  <div class="brand"><span class="brand-name">CORVELLA</span><span class="brand-tag">MANAGEMENT SERVICES</span></div>
  <div class="lh-contact">
    <div class="line"><svg class="icon" width="6" height="6"><use href="#i-doc"/></svg>2016/208317/07</div>
    <div class="line"><svg class="icon" width="6" height="6"><use href="#i-doc"/></svg>4710263558</div>
    <div class="line"><svg class="icon" width="6" height="6"><use href="#i-mail"/></svg>info@corvellams.com</div>
    <div class="line web"><svg class="icon" width="6" height="6"><use href="#i-web"/></svg>www.<span>corvellams</span>.co.za</div>
  </div>
  <div class="lh-footer">
    <div class="office">
      <div class="office-title">HEAD OFFICE</div>
      <div>24 Kestrel Road, Parkview</div>
      <div>Johannesburg, 2193</div>
      <div class="line"><svg class="icon" width="6" height="6"><use href="#i-phone"/></svg>+27 11 502 3391</div>
      <div class="line"><svg class="icon" width="6" height="6"><use href="#i-fax"/></svg>+27 11 374 8820</div>
    </div>
    <div class="office">
      <div class="office-title">PRETORIA OFFICE</div>
      <div>2nd Floor Linden Court, 1140</div>
      <div>Park Street, Hatfield, 0083</div>
      <div class="line"><svg class="icon" width="6" height="6"><use href="#i-phone"/></svg>+27 12 615 2204</div>
      <div class="line"><svg class="icon" width="6" height="6"><use href="#i-fax"/></svg>+27 12 488 1937</div>
    </div>
    <div class="office">
      <div class="office-title">POLOKWANE OFFICE</div>
      <div>7b Grobler Lane,</div>
      <div>Polokwane, 0700</div>
      <div class="line"><svg class="icon" width="6" height="6"><use href="#i-phone"/></svg>+27 15 731 4402</div>
      <div class="line"><svg class="icon" width="6" height="6"><use href="#i-fax"/></svg>+27 15 731 4450</div>
    </div>
  </div>
  <svg class="swoosh" height="27"><use href="#band"/></svg>
</section>

<!-- Letterhead, with letter -->
<section class="sheet letterhead lh-word">
  <div class="brand"><span class="brand-name">CORVELLA</span><span class="brand-tag">MANAGEMENT SERVICES</span></div>
  <div class="lh-contact">
    <div class="line"><svg class="icon" width="6" height="6"><use href="#i-doc"/></svg>2016/208317/07</div>
    <div class="line"><svg class="icon" width="6" height="6"><use href="#i-doc"/></svg>4710263558</div>
    <div class="line"><svg class="icon" width="6" height="6"><use href="#i-mail"/></svg>info@corvellams.com</div>
    <div class="line web"><svg class="icon" width="6" height="6"><use href="#i-web"/></svg>www.<span>corvellams</span>.co.za</div>
  </div>
  <article class="letter">
    <div class="salutation">Dear, Leon R. Whitfield</div>
    <div class="recipient">President<br><br>Suite 204<br>2270 Harbor Avenue<br>Dayton, OH 45402 USA</div>
    <p class="body">Lorem ipsum dolor sit amet, consectetuer adipiscing elit, sed diam nonummy nibh euismod tincidunt ut laoreet dolore magna aliquam erat volutpat. Ut wisi enim ad minim veniam, quis nostrud exerci tation ullamcorper suscipit lobortis nisl ut aliquip ex ea commodo consequat. Lorem ipsum dolor sit amet, cons ectetuer adipiscing elit, sed diam nonummy nibh euismod tincidunt ut laoreet dolore magna aliquam erat volutpat. Ut wisi enim ad minim veniam, quis nostrud exerci tation ullamcorper suscipit lobortis nisl ut aliquip ex ea commodo consequat. Lorem ipsum dolor sit amet, consectetuer adipiscing elit, sed diam nonummy nibh euismod tincidunt ut laoreet dolore magna aliquam erat volutpat. Ut wisi enim ad minim veniam,</p>
    <p class="body">Lorem ipsum dolor sit amet, consectetuer adipiscing elit, sed diam nonummy nibh euismod tincidunt ut laoreet dolore magna aliquam erat volutpat. Ut wisi enim ad minim veniam, quis nostrud exerci tation ullamcorper suscipit lobortis nisl ut aliquip ex ea commodo consequat. Lorem ipsum dolor sit amet, cons ectetuer adipiscing elit, sed diam nonummy nibh euismod tincidunt ut laoreet dolore magna aliquam erat volutpat.</p>
    <p class="body">consequat. Duis autem vel eum iriure dolor in hendrerit in vulputate velit esse molestie consequat, vel illum dolore eu feugiat nulla facilisis at vero eros et accumsan. Duis autem vel eum iriure dolor in hendrerit in vulputate velit esse molestie consequat, vel illum dolore eu feugiat nulla facilisis at vero eros et accumsan</p>
    <div class="closing">Sincerely</div>
    <div class="signature" role="img" aria-label="Handwritten signature of the sender"></div>
  </article>
  <div class="lh-footer">
    <div class="office">
      <div class="office-title">HEAD OFFICE</div>
      <div>24 Kestrel Road, Parkview</div>
      <div>Johannesburg, 2193</div>
      <div class="line"><svg class="icon" width="6" height="6"><use href="#i-phone"/></svg>+27 11 502 3391</div>
      <div class="line"><svg class="icon" width="6" height="6"><use href="#i-fax"/></svg>+27 11 374 8820</div>
    </div>
    <div class="office">
      <div class="office-title">PRETORIA OFFICE</div>
      <div>2nd Floor Linden Court, 1140</div>
      <div>Park Street, Hatfield, 0083</div>
      <div class="line"><svg class="icon" width="6" height="6"><use href="#i-phone"/></svg>+27 12 615 2204</div>
      <div class="line"><svg class="icon" width="6" height="6"><use href="#i-fax"/></svg>+27 12 488 1937</div>
    </div>
    <div class="office">
      <div class="office-title">POLOKWANE OFFICE</div>
      <div>7b Grobler Lane,</div>
      <div>Polokwane, 0700</div>
      <div class="line"><svg class="icon" width="6" height="6"><use href="#i-phone"/></svg>+27 15 731 4402</div>
      <div class="line"><svg class="icon" width="6" height="6"><use href="#i-fax"/></svg>+27 15 731 4450</div>
    </div>
  </div>
  <svg class="swoosh" height="27"><use href="#band"/></svg>
</section>

<div class="label label-plain">Letterhead</div>
<div class="label label-word">Word Document Letterhead</div>

<!-- Email signature -->
<section class="sheet email-signature">
  <div class="brand"><span class="brand-name">CORVELLA</span><span class="brand-tag">MANAGEMENT SERVICES</span></div>
  <div class="sig-divider"></div>
  <div class="sig-details">
    <div class="person">DANIEL OKORO</div>
    <div class="role">HEAD OF ICT</div>
    <div>24 Kestrel Road, Parkview</div>
    <div>Johannesburg, 2193</div>
    <div class="line"><svg class="icon" width="10" height="10"><use href="#i-phone"/></svg>085 410 7723</div>
    <div class="line"><svg class="icon" width="10" height="10"><use href="#i-phone"/></svg>011 502 3391</div>
    <div class="line"><svg class="icon" width="10" height="10"><use href="#i-mail"/></svg>it@corvellams.com</div>
    <div class="line web"><svg class="icon" width="10" height="10"><use href="#i-web"/></svg>www.corvellams.com</div>
  </div>
  <svg class="swoosh" height="56"><use href="#band"/></svg>
  <div class="social" aria-label="Social media links"><span></span><span></span><span></span><span></span></div>
</section>

</body>
</html>
```